Business Card Design

We would like a business card that utilizes our current logo and keeps with the same feel - elegant and organic. Our farm isn't about mass production, it's about excellence, education, beautiful events and flowers - people, culture, and community.

Target Market(s)

Patrons to our farm who are interested in weddings, events, or our flowers and vegetables.

Contact Information for Business Card

Name, address, cell email (Danielle Hoskins, 2716 Wrenfield Rd, Harlow Springs, ND 58991, cell 555.412.6638, email danielle@wrenfieldacres.com)

```html
<!DOCTYPE html>
<html lang="en">
<head>
<meta charset="utf-8">
<title>Wrenfield Acres – Business Card</title>
<link href="https://fonts.googleapis.com/css2?family=Montserrat:wght@400;500;600&display=swap" rel="stylesheet">
<style>
  :root {
    --backdrop: #3e4f40;
    --sage: #738a72;
    --sage-deep: #3f5240;
    --paper: #fbfbf9;
    --green-text: #5f7a62;
    --grey-text: #707570;
    --earth: #8c6a45;
  }
  * { margin: 0; padding: 0; box-sizing: border-box; }
  html, body {
    width: 1200px; height: 1200px; overflow: hidden;
    background: var(--backdrop);
    font-family: "Montserrat", Arial, sans-serif;
  }
  .card {
    position: absolute; left: 249px;
    width: 698px; height: 390px;
  }
  .card--front { top: 142px; background: var(--sage); }
  .card--back { top: 662px; background: var(--paper); }

  .wordmark {
    position: absolute;
    font-weight: 500;
    letter-spacing: 0.04em;
    white-space: nowrap;
    display: flex; align-items: center; gap: 12px;
  }
  .wordmark__dot { width: 12px; height: 12px; border-radius: 50%; }
  .card--front .wordmark {
    left: 0; right: 0; top: 172px; justify-content: center;
    font-size: 40px; color: var(--sage-deep);
  }
  .card--front .wordmark__dot { background: var(--sage-deep); }
  .card--back .wordmark {
    left: 366px; top: 92px;
    font-size: 29px; color: var(--green-text);
  }
  .card--back .wordmark__dot { background: var(--green-text); width: 10px; height: 10px; }

  .tab {
    position: absolute; left: 0; top: 165px;
    width: 17px; height: 55px;
    background: var(--sage); border-radius: 0 4px 4px 0;
  }
  .person { position: absolute; left: 47px; top: 168px; }
  .person__name {
    font-weight: 600; font-size: 22px; color: var(--green-text);
    letter-spacing: 0.01em; text-transform: uppercase; line-height: 26px;
  }
  .person__role { font-size: 17px; color: var(--grey-text); line-height: 22px; }

  .contact {
    position: absolute; left: 366px; top: 236px;
    font-size: 17px; color: var(--grey-text); line-height: 23px;
  }
  .contact__address { font-style: normal; }
  .contact__lines { list-style: none; margin-top: 14px; }
  .contact__lines li { display: flex; align-items: center; gap: 8px; }
  .contact__icon { width: 15px; height: 15px; flex: none; }
</style>
</head>
<body>
  <section class="card card--front">
    <div class="wordmark"><span class="wordmark__dot"></span>Wrenfield Acres</div>
  </section>

  <section class="card card--back">
    <div class="wordmark"><span class="wordmark__dot"></span>Wrenfield Acres</div>
    <div class="tab"></div>
    <div class="person">
      <p class="person__name">Danielle Hoskins</p>
      <p class="person__role">Founder &amp; CEO</p>
    </div>
    <div class="contact">
      <address class="contact__address">2716 Wrenfield Rd,<br>Harlow Springs, ND 58991</address>
      <ul class="contact__lines">
        <li>
          <svg class="contact__icon" viewBox="0 0 24 24" aria-hidden="true"><path fill="var(--earth)" d="M6.6 10.8a15 15 0 0 0 6.6 6.6l2.2-2.2a1 1 0 0 1 1-.25 11.4 11.4 0 0 0 3.6.57 1 1 0 0 1 1 1V20a1 1 0 0 1-1 1A17 17 0 0 1 3 4a1 1 0 0 1 1-1h3.5a1 1 0 0 1 1 1c0 1.25.2 2.45.57 3.57a1 1 0 0 1-.25 1z"/></svg>
          555.412.6638
        </li>
        <li>
          <svg class="contact__icon" viewBox="0 0 24 24" aria-hidden="true"><rect x="2" y="5" width="20" height="14" rx="1.5" fill="var(--earth)"/><path d="M3 6l9 7 9-7" fill="none" stroke="var(--paper)" stroke-width="1.6"/></svg>
          danielle@wrenfieldacres.com
        </li>
      </ul>
    </div>
  </section>
</body>
</html>
```